Hi, I am looking for email marketing freelancer who can come up with a Christmas design and then cut the design as EDM for sending to clients.
Dont want only designer. The person also needs to slice it so that it can go as email. Attaching our logo to match the template

```html
<!DOCTYPE html>
<html lang="en">
<head>
<meta charset="utf-8">
<title>Northpeak Christmas Newsletter</title>
<link rel="stylesheet" href="https://fonts.googleapis.com/css2?family=Oswald:wght@400&family=Arimo:wght@400;700&family=Tinos:ital,wght@1,700&display=swap">
<style>
  :root {
    --backdrop: #4a4a4a;
    --card-red: #b82424;
    --panel-red: #d14b4b;
    --ribbon: #e85b5e;
    --ribbon-dark: #a82c33;
    --gold: #f2c14e;
    --text-light: #fbe3e3;
    --text-dark: #3b3b3b;
    --heading-red: #d9383a;
    --white: #ffffff;
    --snow: #e8eef2;
    --badge: #7a4a32;
  }
  * { box-sizing: border-box; margin: 0; padding: 0; }
  html, body { width: 1200px; height: 1200px; overflow: hidden; }
  body {
    background: var(--backdrop);
    font-family: "Arimo", Arial, sans-serif;
    position: relative;
  }
  .newsletter {
    position: absolute; left: 165px; top: 39px;
    width: 872px; height: 1096px;
    background: var(--card-red);
  }
  .newsletter__column {
    position: absolute; left: 107px; top: 0;
    width: 657px; height: 100%;
  }
  .brand {
    position: absolute; left: 1px; top: 1px;
    width: 180px; height: 180px;
    background: var(--white);
    display: flex; align-items: center; justify-content: center; gap: 8px;
    font-family: "Arimo", Arial, sans-serif; font-weight: 700;
    font-size: 24px; color: #2a2a2a; z-index: 3;
  }
  .brand__dot { width: 14px; height: 14px; background: #1f7a2a; }
  .social {
    position: absolute; top: 17px; left: 456px;
    display: flex; gap: 12px; z-index: 3;
  }
  .social__item {
    width: 58px; height: 58px; border-radius: 50%;
    background: rgba(255,255,255,0.22);
  }
  .hero {
    position: absolute; left: 0; top: 98px;
    width: 661px; height: 663px;
    background: var(--panel-red);
  }
  .hero__art {
    position: absolute; left: 128px; top: -37px;
    width: 400px; height: 380px;
    background: radial-gradient(ellipse at 50% 55%, #f4c25a 0%, #e9a24f 35%, rgba(209,75,75,0) 70%);
  }
  .hero__ribbon {
    position: absolute; left: 168px; top: 336px;
    width: 320px; height: 66px;
    background: var(--ribbon);
    display: flex; align-items: center; justify-content: center;
    font-family: "Oswald", sans-serif; font-size: 34px;
    color: var(--white); letter-spacing: 0.5px;
  }
  .hero__ribbon::before, .hero__ribbon::after {
    content: ""; position: absolute; top: 14px;
    width: 36px; height: 48px; background: var(--ribbon-dark); z-index: -1;
  }
  .hero__ribbon::before { left: -28px; }
  .hero__ribbon::after { right: -28px; }
  .hero__text {
    position: absolute; left: 32px; top: 459px; width: 625px;
    font-size: 14.5px; line-height: 24px; color: var(--text-light);
  }
  .winter-scene {
    position: absolute; left: 0; top: 700px;
    width: 657px; height: 168px;
    background: linear-gradient(180deg, rgba(255,255,255,0) 0%, #dfe7ec 45%, var(--snow) 70%, var(--white) 100%);
  }
  .feature {
    position: absolute; left: 0; top: 868px;
    width: 657px; height: 228px;
    background: var(--white);
  }
  .feature__title {
    position: absolute; left: 32px; top: 36px;
    font-family: "Tinos", "Times New Roman", serif;
    font-style: italic; font-weight: 700;
    font-size: 23px; color: var(--heading-red);
  }
  .feature__text {
    position: absolute; left: 32px; top: 72px; width: 455px;
    font-size: 14.5px; line-height: 24px; color: var(--text-dark);
  }
  .feature__badge {
    position: absolute; left: 524px; top: 62px;
    width: 93px; height: 108px;
    background: var(--badge);
    clip-path: polygon(0 0, 100% 0, 100% 100%, 50% 85%, 0 100%);
  }
</style>
</head>
<body>
  <main class="newsletter">
    <div class="newsletter__column">
      <section class="hero">
        <div class="hero__art" role="img" aria-label="Golden Christmas tree illustration with star, two reindeer, gift box and falling snow"></div>
        <h1 class="hero__ribbon">MERRY CHRISTMAS!</h1>
        <p class="hero__text">Lorem ipsum dolor sit amet, consectetur adipiscing elit. Curabitur elementum eleifend vestibulum. Fusce dignissim malesuada nunc, eu dapibus purus accumsan nec. Pellentesque in suscipit nisl, a pharetra ante. Quisque venenatis nisi at sollicitudin porttitor. Nullam mollis euismod pretium.</p>
      </section>
      <div class="brand"><span class="brand__dot"></span>Northpeak</div>
      <nav class="social" aria-label="Social links">
        <span class="social__item"></span>
        <span class="social__item"></span>
        <span class="social__item"></span>
      </nav>
      <div class="winter-scene" role="img" aria-label="Snowy hills with white frosted pine trees"></div>
      <section class="feature">
        <h2 class="feature__title">Santa Claus is Coming to Town</h2>
        <p class="feature__text">Lorem ipsum dolor sit amet, consectetur adipiscing elit. Curabitur elementum eleifend vestibulum. Fusce dignissim malesuada nunc, eu dapibus purus accumsan nec. Pellentesque in suscipit nisl, a pharetra ante. Quisque venenatis nisi at sollicitudin porttitor. Nullam mollis euismod pretium.</p>
        <div class="feature__badge" role="img" aria-label="Hot pick badge with bell and bow"></div>
      </section>
    </div>
  </main>
</body>
</html>
```